Halvern Mechanical Contractors needs a Website

Create basic website for commercial plumbing and mechanical contractor; to include pictures of works in progress and completed works, description of all services offered and geographical locations and licenses

Target Market(s)

General Contractors, Real Estate Developers, Construction Companies

Industry/Entity Type

Construction

Coding

Coded - Design and coding required

Number of Pages Required

5+ page

Font styles to use
Other font styles liked:
• See logo attached to project

Colors
0392cd

```html
<!DOCTYPE html>
<html lang="en">
<head>
<meta charset="utf-8">
<title>Halvern Mechanical Contractors</title>
<link href="https://fonts.googleapis.com/css2?family=Ubuntu:wght@300;400;500;700&display=swap" rel="stylesheet">
<style>
:root{
  --blue:#0392cd;
  --blue-dark:#0a7fb8;
  --navy:#1c2a3a;
  --ink:#222;
  --text:#555;
  --grey-bg:#efefef;
  --paper:#f2f1ee;
  --footer-dark:#121418;
  --white:#fff;
}
*{margin:0;padding:0;box-sizing:border-box}
html,body{width:742px;height:1200px;overflow:hidden}
body{position:relative;font-family:'Ubuntu',sans-serif;background:var(--white);color:var(--text)}
.abs{position:absolute}
.topline{left:0;top:0;width:742px;height:2px;background:var(--blue)}
.brand{left:69px;top:28px;display:flex;align-items:center;gap:8px}
.brand-mark{width:30px;height:30px;border-radius:50%;background:var(--blue)}
.brand-name{font-weight:700;font-size:11px;line-height:11px;color:var(--navy);text-transform:uppercase;width:90px}
.contact-top{top:56px;display:flex;align-items:center;gap:6px;font-size:10px;color:#777}
.contact-top svg{width:24px;height:24px}
.paper{left:0;top:91px;width:742px;height:295px;background:var(--paper)}
.nav{left:69px;top:91px;width:604px;height:39px;background:linear-gradient(#1ea3dc,var(--blue-dark));display:flex;align-items:center;padding-left:12px}
.nav a{color:var(--white);text-decoration:none;font-size:8px;font-weight:500;text-transform:uppercase;padding:0 19px;line-height:39px;border-right:1px solid rgba(255,255,255,.15)}
.nav a.current{border:1px solid rgba(255,255,255,.8);border-radius:13px;line-height:24px;padding:0 13px;margin-right:13px}
.nav a:last-child{border-right:0}
.hero{left:69px;top:130px;width:604px;height:256px;background:linear-gradient(100deg,#7d8a96 0%,#b8c3cc 35%,#3b4a66 65%,#1d2a4a 100%)}
.caption{left:89px;top:295px;width:222px;height:71px;background:rgba(40,40,40,.82);padding:14px 24px;color:var(--white)}
.caption h2{font-weight:400;font-size:13px;margin-bottom:6px}
.caption p{font-size:6.5px;line-height:13px;color:#ddd}
.arrows{left:593px;top:352px;width:80px;height:34px;background:rgba(20,20,20,.6);display:flex;justify-content:space-around;align-items:center;color:var(--white);font-size:10px}
.section-title{left:0;width:742px;text-align:center;font-weight:700;font-size:19px;color:var(--navy);display:flex;justify-content:center;align-items:center;gap:4px}
.section-title .dot{width:20px;height:20px;border-radius:50%;background:var(--blue)}
.welcome-text{left:78px;top:450px;width:586px;text-align:center;font-size:6.5px;line-height:19px;color:#555}
.services-bg{left:0;top:529px;width:742px;height:283px;background:var(--grey-bg)}
.card{top:603px;width:138px}
.card .photo{height:94px;border:2px solid var(--white);box-shadow:0 3px 4px rgba(0,0,0,.2)}
.card h3{margin-top:21px;font-size:9px;font-weight:500;color:var(--blue);text-transform:uppercase}
.card p{margin-top:5px;font-size:6.5px;line-height:16px;color:#666;text-align:justify}
.post{top:882px;display:flex;gap:11px}
.post .photo{width:109px;height:77px;position:relative;border:2px solid var(--white);box-shadow:0 3px 4px rgba(0,0,0,.2)}
.post .date{position:absolute;right:0;bottom:0;background:var(--blue);color:var(--white);font-size:7.5px;padding:4px 6px}
.post .lead{font-size:8px;line-height:16px;color:#444;text-align:justify}
.post .sub{font-size:6.5px;line-height:16px;color:#777;text-align:justify;margin-top:3px}
.footer{left:0;top:994px;width:742px;height:157px;background:var(--blue);color:var(--white)}
.footer h4{position:absolute;font-size:10.5px;font-weight:500;text-transform:uppercase}
.field{position:absolute;border:1px solid rgba(255,255,255,.8);font-size:6.5px;padding:8px 7px}
.submit{position:absolute;left:291px;top:107px;width:70px;height:26px;background:#111;color:var(--white);font-size:9px;font-weight:500;text-align:center;line-height:26px;border-radius:2px}
.divider{position:absolute;top:20px;width:1px;height:120px;background:rgba(255,255,255,.2)}
.info{position:absolute;left:401px;font-size:6.5px;line-height:12px;display:flex;gap:7px}
.info svg{width:9px;height:9px;flex:none;margin-top:2px}
.links{position:absolute;left:572px;top:60px;font-size:6.5px;line-height:19px}
.bottom{left:0;top:1151px;width:742px;height:49px;background:var(--footer-dark);font-size:6.5px;color:#ccc}
.bottom .copy{position:absolute;left:69px;top:20px}
.bottom .copy span{color:var(--blue);margin-left:6px}
.social{position:absolute;left:614px;top:19px;display:flex;gap:4px}
.social i{width:12px;height:12px;border-radius:50%;background:var(--blue)}
.social i:last-child{background:#d6453b}
.social i:nth-child(3){background:#c33}
</style>
</head>
<body>
<div class="abs topline"></div>
<header>
  <div class="abs brand"><span class="brand-mark"></span><span class="brand-name">Halvern Mechanical Contractors</span></div>
  <div class="abs contact-top" style="left:422px">
    <svg viewBox="0 0 24 24"><circle cx="12" cy="12" r="11" fill="none" stroke="#1c2a3a" stroke-width="1.5"/><path d="M8 7l2 0 1 3-1.5 1a6 6 0 0 0 3 3l1-1.5 3 1 0 2a2 2 0 0 1-2 1A9 9 0 0 1 7 9a2 2 0 0 1 1-2z" fill="#1c2a3a"/></svg>
    <span>000 987 654 321</span></div>
  <div class="abs contact-top" style="left:538px">
    <svg viewBox="0 0 24 24"><circle cx="12" cy="12" r="11" fill="none" stroke="#1c2a3a" stroke-width="1.5"/><rect x="7" y="8" width="10" height="8" fill="#1c2a3a"/><path d="M7 8l5 4 5-4" fill="none" stroke="#fff"/></svg>
    <span>info@domainname.com</span></div>
</header>
<div class="abs paper"></div>
<nav class="abs nav">
  <a class="current">Home</a><a>About Us</a><a>Services</a><a>News &amp; Events</a><a>Testimonials</a><a>Blog</a><a>Contact Us</a>
</nav>
<div class="abs hero" role="img" aria-label="Technician in blue overalls checking a clipboard beside blue plant-room pipework and gauges"></div>
<div class="abs caption"><h2>FULL PLUMBING SERVICES</h2><p>Lorem ipsum dolor sit amet, consectetur adipiscing elit.<br>In non nisi libero. Suspendisse eget orci.</p></div>
<div class="abs arrows"><span>&#8249;</span><span>&#8250;</span></div>

<h2 class="abs section-title" style="top:417px"><span class="dot"></span>WELCOME TO OUR SITE</h2>
<p class="abs welcome-text">Lorem ipsum dolor sit amet, consectetur adipiscing elit. In non nisi libero. Suspendisse eget orci quis ipsum pellentesque venenatis quis non diam. Etiam eu ante leo. Mauris quis congue nisl. Nulla eros magna, blandit eu hendrerit ac, ultrices id ipsum. Donec nulla risus, eleifend elementum augue sit amet, ultrices aliquam est. Pellentesque aliquet justo at felis fermentum molestie. Fusce aliquet vel ipsum eget egestas. Curabitur lectus leo, bibendum at mollis ut, tincidunt in metus.</p>

<div class="abs services-bg"></div>
<h2 class="abs section-title" style="top:553px"><span class="dot"></span>OUR SERVICES</h2>
<div class="abs card" style="left:69px"><div class="photo" role="img" aria-label="Hands fitting a pipe joint under a sink" style="background:linear-gradient(135deg,#8a6a4a,#c9b9a4,#3a3a3a)"></div><h3>Commercial Plumbing</h3><p>Claritas est etiam processus dynamicus, qui sequitur mutationem consuetudium lecto rum mirum est notare quam.</p></div>
<div class="abs card" style="left:225px"><div class="photo" role="img" aria-label="Engineer among rows of industrial valves and pumps" style="background:linear-gradient(135deg,#6b7a6e,#b0b8b4,#4a5a5e)"></div><h3>Industrial Plumbing</h3><p>Lorem ipsum dolor sit amet, consectetur adipiscing elit. Proin sollicitudin urna quis dolor hendrerit interdum.</p></div>
<div class="abs card" style="left:380px"><div class="photo" role="img" aria-label="Worker in hard hat inspecting large steel pipework" style="background:linear-gradient(135deg,#c8c8c8,#a84a4a,#d0d0d0)"></div><h3>Condominiums</h3><p>Donec elit dolor, bibendum in enim ac, congue imperdiet enim. Quisque efficitur, purus eget laoreet dignissim.</p></div>
<div class="abs card" style="left:535px"><div class="photo" role="img" aria-label="Plumber on the phone holding a clipboard beside a boiler" style="background:linear-gradient(135deg,#e6e6e6,#3a5a9a,#f0f0f0)"></div><h3>Help &amp; Advice</h3><p>Morbi cursus at nunc ornare mattis. In nec tellus nec nisl finibus egestas. Donec vulput ate justo vel ante dapibus.</p></div>

<h2 class="abs section-title" style="top:836px"><span class="dot"></span>OUR BLOG</h2>
<article class="abs post" style="left:70px;width:293px">
  <div class="photo" role="img" aria-label="Long corridor of industrial pipes" style="background:linear-gradient(135deg,#5a6a7a,#b0b6c0,#c47a3a)"><span class="date">20 Jun 2016</span></div>
  <div style="width:173px"><p class="lead">Ut eleifend augue dolor, nec convallis dolor feug iat eget. Donec sit amet lorem.</p><p class="sub">Vestibulum rhoncus ligula nisi, nec mollis ex hendrerit ut. Proin tellus mauris, condimentum a purus sed, conse ctetur congue est. Proin sollicitudin...</p></div>
</article>
<article class="abs post" style="left:379px;width:294px">
  <div class="photo" role="img" aria-label="Close-up of water meters with splashing water" style="background:linear-gradient(135deg,#2a5a8a,#9ac4dc,#3a6a9a)"><span class="date">19 Jun 2016</span></div>
  <div style="width:174px"><p class="lead">Proin sollicitudin condimentum mattis. Integer at eros laoreet, gravida ante nec, rhoncus elit.</p><p class="sub">Aenean lacus arcu, interdum non elementum sed, port titor in purus. Sed quis nibh a lacus cursus pellent esque. Vivamus eget quam ac lectus...</p></div>
</article>

<footer class="abs footer">
  <h4 style="left:70px;top:18px">Contact Us</h4>
  <div class="field" style="left:69px;top:41px;width:111px;height:26px">Name</div>
  <div class="field" style="left:69px;top:73px;width:111px;height:26px">Email Address</div>
  <div class="field" style="left:69px;top:105px;width:111px;height:26px">Phone</div>
  <div class="field" style="left:191px;top:41px;width:170px;height:58px">Message</div>
  <div class="submit">SUBMIT</div>
  <div class="divider" style="left:382px"></div>
  <h4 style="left:401px;top:18px">Get In Touch</h4>
  <div class="info" style="top:44px"><svg viewBox="0 0 10 10"><path d="M5 0a3.5 3.5 0 0 1 3.5 3.5C8.5 6 5 10 5 10S1.5 6 1.5 3.5A3.5 3.5 0 0 1 5 0z" fill="#fff"/><circle cx="5" cy="3.5" r="1.3" fill="#0392cd"/></svg><span>COMPANY NAME<br>123, Lorem Ipsm, Lorem Ipsm<br>Lorem Ipsm - 123 456</span></div>
  <div class="info" style="top:93px"><svg viewBox="0 0 10 10"><rect y="1.5" width="10" height="7" fill="#fff"/><path d="M0 1.5l5 4 5-4" fill="none" stroke="#0392cd"/></svg><span>info@domainname.com</span></div>
  <div class="info" style="top:114px"><svg viewBox="0 0 10 10"><rect width="10" height="10" rx="2" fill="#fff"/><path d="M3 2h1.3l.6 1.8-.9.7a3.5 3.5 0 0 0 1.5 1.5l.7-.9L8 5.7V7a1 1 0 0 1-1 1A5 5 0 0 1 2 3a1 1 0 0 1 1-1z" fill="#0392cd"/></svg><span>+123 456 789 000</span></div>
  <div class="divider" style="left:546px"></div>
  <h4 style="left:571px;top:18px">Quick Links</h4>
  <div class="links">Services<br>Testimonials<br>News &amp; Events<br>Blog<br>Contact Us</div>
</footer>
<div class="abs bottom">
  <p class="copy">Copyright &copy; 2016 <b style="font-weight:400;color:#fff">COMPANY NAME</b>. All Rights Reserved. <span>Privacy Policy</span> <span>Terms of Service</span></p>
  <div class="social"><i></i><i></i><i></i><i></i></div>
</div>
</body>
</html>
```